Design for Certificate

Design a certificate for training, providing our company logo such as attachments. Company's name is "BRYNE Fjellvik Advisory Ltd", please refer to our company profile: https://www.bryne-fjellvik.example/company_info

The style of the current certificate is also attached, and another certificate of another company can be referred to. Psd & jpg are required for the final draft (the layers of psd are not merged). Thanks!

```html
<!DOCTYPE html>
<html lang="en">
<head>
<meta charset="utf-8">
<title>Certificate of Completion – BRYNE Fjellvik Advisory Ltd</title>
<link rel="stylesheet" href="https://fonts.googleapis.com/css2?family=Oswald:wght@600;700&family=Crimson+Pro:wght@600;700&display=swap">
<style>
  :root {
    --backdrop: #2e3133;
    --paper: #f7ede4;
    --gold: #e4b54b;
    --banner: #363b3c;
    --banner-name: #dcae8e;
    --ink: #35393b;
  }
  html, body {
    margin: 0;
    width: 1200px;
    height: 1200px;
    overflow: hidden;
    background: var(--backdrop);
  }
  .certificate {
    position: absolute;
    left: 212px;
    top: 50px;
    width: 776px;
    height: 1100px;
    background: var(--paper);
    color: var(--ink);
    font-family: "Crimson Pro", Georgia, serif;
    font-weight: 700;
    box-shadow: 0 10px 30px rgba(0,0,0,.35);
  }
  .abs { position: absolute; }
  .rule-h {
    position: absolute;
    height: 2px;
    border-top: 3px solid var(--gold);
    border-bottom: 2px solid var(--gold);
  }
  .rule-v {
    position: absolute;
    width: 2px;
    border-left: 3px solid var(--gold);
    border-right: 2px solid var(--gold);
  }
  .corner-ornament {
    position: absolute;
    width: 54px;
    height: 54px;
    border-radius: 50%;
    background: radial-gradient(circle at 40% 40%, #edc664, #cf9d33);
  }
  .banner {
    position: absolute;
    left: 266px;
    top: 0;
    width: 245px;
    height: 238px;
  }
  .banner-name {
    position: absolute;
    left: 266px;
    top: 86px;
    width: 245px;
    text-align: center;
    font-family: "Oswald", sans-serif;
    font-weight: 600;
    font-size: 62px;
    letter-spacing: 4px;
    color: var(--banner-name);
    line-height: 1;
  }
  .centered {
    position: absolute;
    left: 0;
    width: 100%;
    text-align: center;
    line-height: 1;
  }
  .title {
    top: 278px;
    font-family: "Oswald", sans-serif;
    font-weight: 700;
    font-size: 58px;
    letter-spacing: -0.5px;
  }
  .awarded { top: 380px; font-size: 35px; }
  .completed { top: 550px; font-size: 28px; }
  .fill-line {
    position: absolute;
    border-bottom: 3px dotted var(--ink);
    height: 0;
  }
  .text { position: absolute; line-height: 1; white-space: nowrap; }
  .course-label { left: 475px; top: 634px; font-size: 30px; }
  .hours-label { left: 114px; top: 713px; font-size: 30px; }
  .issuer-name { left: 83px; top: 840px; font-size: 36px; letter-spacing: .5px; }
  .signer-role { left: 433px; width: 257px; text-align: center; top: 880px; font-size: 20px; }
  .cert-no-label { left: 56px; top: 944px; font-size: 20px; }
</style>
</head>
<body>
  <main class="certificate">
    <!-- frame rules -->
    <div class="rule-h" style="left:95px; top:60px; width:171px;"></div>
    <div class="rule-h" style="left:511px; top:60px; width:169px;"></div>
    <div class="rule-h" style="left:95px; top:1028px; width:585px;"></div>
    <div class="rule-v" style="left:22px; top:86px; height:925px;"></div>
    <div class="rule-v" style="left:747px; top:86px; height:925px;"></div>

    <div class="corner-ornament" role="img" aria-label="Gold crown corner ornament" style="left:28px; top:24px;"></div>
    <div class="corner-ornament" role="img" aria-label="Gold crown corner ornament" style="left:694px; top:24px;"></div>
    <div class="corner-ornament" role="img" aria-label="Gold crown corner ornament" style="left:28px; top:1020px;"></div>
    <div class="corner-ornament" role="img" aria-label="Gold crown corner ornament" style="left:694px; top:1020px;"></div>

    <svg class="banner" viewBox="0 0 245 238" aria-hidden="true">
      <polygon points="0,0 245,0 245,238 122.5,200 0,238" fill="var(--banner)"/>
    </svg>
    <div class="banner-name">BRYNE</div>

    <h1 class="centered title" style="margin:0;">CERTIFICATE OF COMPLETION</h1>
    <p class="centered awarded" style="margin:0;">this certificate is awarded to</p>
    <div class="fill-line" style="left:114px; top:522px; width:546px;"></div>
    <p class="centered completed" style="margin:0;">has successfully completed</p>

    <div class="fill-line" style="left:57px; top:654px; width:405px;"></div>
    <span class="text course-label">Training Course</span>

    <span class="text hours-label">Sixteen hours, held on</span>
    <div class="fill-line" style="left:408px; top:726px; width:250px;"></div>

    <span class="text issuer-name">BRYNE FJELLVIK</span>
    <div class="fill-line" style="left:433px; top:859px; width:257px;"></div>
    <span class="text signer-role">Chief Technology Officer</span>

    <span class="text cert-no-label">Certificate No:</span>
    <div class="fill-line" style="left:202px; top:959px; width:220px;"></div>
  </main>
</body>
</html>
```